Crash Reapirer business card design

We are a crash repair business based in a small country town in South Australia with our own spray booth. We do all types of repairs for both insurance companies and private jobs. We also replace broken windscreens.
We usually have the KTV logo on our cards because we are KTV approved repairers.
We would also like the BLQ (Vehicle Guild Council)logo because we are a member for them also.
If the card could incorporate black, grey, white and silver colours that would be excellent.
We do not have our own logo if 1 could be created that would be great.

Industry/Entity Type

Insurance

Contact Information for Business Card

Dorvick Crash Repairs
47 Tallowood Ave, Renmark SA 5341
Ph 08 85127730 Fax 08 85127856
Owen 0412658304
Email - dorcrash@wexmail.example

We do private & insurance work, windscreen replacements on all makes & models of cars

```html
<!DOCTYPE html>
<html lang="en">
<head>
<meta charset="utf-8">
<title>Dorvick Crash Repairs – Business Card</title>
<link rel="stylesheet" href="https://fonts.googleapis.com/css2?family=Michroma&family=Jura:wght@500;600;700&display=swap">
<style>
  :root {
    --backdrop: #d8d8d5;
    --card-white: #ffffff;
    --card-mist: #e4e4e6;
    --brand-blue: #3b3f97;
    --ribbon-grey: #8a8a8c;
    --ribbon-shade: #555557;
    --ribbon-fold: #6d6d70;
    --ink-dark: #2b2b2d;
    --ink-light: #ffffff;
  }
  * { box-sizing: border-box; margin: 0; padding: 0; }
  html, body { width: 1200px; height: 869px; overflow: hidden; }
  body { background: var(--backdrop); position: relative; font-family: "Jura", sans-serif; }

  .card {
    position: absolute;
    width: 560px;
    height: 320px;
    box-shadow: 0 10px 24px rgba(0,0,0,.25);
    overflow: hidden;
  }
  .card-back {
    left: 80px; top: 90px;
    background: linear-gradient(135deg, var(--card-white) 30%, var(--card-mist));
  }
  .card-front { left: 560px; top: 430px; background: var(--card-white); }
  .card-art { position: absolute; inset: 0; }

  .brand-name {
    position: absolute;
    font-family: "Michroma", sans-serif;
    color: var(--brand-blue);
    font-size: 19px;
    white-space: nowrap;
  }
  .card-back .brand-name { left: 120px; top: 148px; }
  .card-front .brand-name { left: 40px; top: 40px; }

  .address {
    position: absolute; left: 122px; top: 120px;
    color: var(--ink-light); font-size: 13px; font-weight: 600; letter-spacing: .3px;
    white-space: nowrap;
  }
  .person {
    position: absolute; right: 20px; top: 140px; text-align: right; color: var(--ink-dark);
    white-space: nowrap;
  }
  .person-name { font-size: 18px; font-weight: 700; letter-spacing: 1px; line-height: 1.1; }
  .person-role { font-size: 9.5px; font-weight: 600; letter-spacing: 1.2px; margin-top: 2px; }

  .contact {
    position: absolute; color: var(--ink-light);
    font-size: 14px; font-weight: 600; letter-spacing: .8px; white-space: nowrap;
  }
  .contact-web { left: 70px; top: 174px; }
  .contact-mail { left: 70px; top: 206px; }
  .contact-phone { left: 380px; top: 220px; }
  .contact-mobile { left: 380px; top: 252px; }
</style>
</head>
<body>

<section class="card card-back" aria-label="Card back">
  <p class="brand-name">Dorvick Crash Repairs</p>
</section>

<section class="card card-front" aria-label="Card front">
  <svg class="card-art" width="560" height="320" viewBox="0 0 560 320" aria-hidden="true">
    <defs>
      <linearGradient id="topSheen" x1="0" y1="0" x2="1" y2="1">
        <stop offset="0" stop-color="#ffffff"/>
        <stop offset="1" stop-color="#e2e2e4"/>
      </linearGradient>
      <linearGradient id="steel" x1="0" y1="0" x2="1" y2="0">
        <stop offset="0" stop-color="#2a2a2c"/>
        <stop offset=".45" stop-color="#b5b5b7"/>
        <stop offset=".7" stop-color="#6e6e70"/>
        <stop offset="1" stop-color="#2a2a2c"/>
      </linearGradient>
    </defs>
    <rect width="560" height="320" fill="url(#topSheen)"/>
    <!-- blue band -->
    <polygon points="0,128 370,128 398,188 560,188 560,290 0,290" fill="var(--brand-blue)"/>
    <!-- steel base -->
    <rect x="0" y="290" width="560" height="30" fill="url(#steel)"/>
    <!-- address ribbon -->
    <polygon points="100,128 110,142 110,114" fill="var(--ribbon-shade)"/>
    <polygon points="110,112 360,112 360,146 110,146" fill="var(--ribbon-grey)"/>
    <polygon points="340,146 360,112 398,188 372,188" fill="var(--ribbon-fold)"/>
    <!-- icon tiles -->
    <g fill="#ffffff">
      <rect x="40" y="170" width="22" height="22" rx="3"/>
      <rect x="40" y="202" width="22" height="22" rx="3"/>
      <rect x="350" y="216" width="22" height="22" rx="3"/>
      <rect x="350" y="248" width="22" height="22" rx="3"/>
    </g>
    <g fill="none" stroke="var(--brand-blue)" stroke-width="1.4">
      <circle cx="51" cy="181" r="7"/>
      <ellipse cx="51" cy="181" rx="3" ry="7"/>
      <line x1="44" y1="181" x2="58" y2="181"/>
      <rect x="44" y="208" width="14" height="10"/>
      <polyline points="44,208 51,214 58,208"/>
    </g>
    <path d="M356 221 q2 -1 3 1 l1 3 q0 2 -2 2 q1 4 5 6 q0 -2 2 -2 l3 1 q2 1 1 3 q-2 3 -5 2 q-7 -3 -9 -11 q-1 -3 1 -5z" fill="var(--brand-blue)"/>
    <rect x="356" y="251" width="10" height="16" rx="2" fill="var(--brand-blue)"/>
    <rect x="358" y="254" width="6" height="9" fill="#ffffff"/>
  </svg>

  <p class="brand-name">Dorvick Crash Repairs</p>
  <p class="address">47 Tallowood Ave, Renmark SA 5341</p>

  <div class="person">
    <p class="person-name">OWEN HARTLEY</p>
    <p class="person-role">GENERAL MANAGER</p>
  </div>

  <p class="contact contact-web">www.dorvickrepairs.example</p>
  <p class="contact contact-mail">dorcrash@wexmail.example</p>
  <p class="contact contact-phone">08 85127730</p>
  <p class="contact contact-mobile">0412658304</p>
</section>

</body>
</html>
```